Morden, Creative, Unique, Independent Wine Shop

1. We are a brand new wine shop located in Melbourne Australia, we have our logo already, simply use the logo to design a business card.
2. I have uploaded our logo in two versions, with or without shadow, any of them is acceptable.
3. Make it as creative and unique as possible, no limitation of shape, color combination, geometry pattern, fonts, composing etc.
3. Info on the card:
- Brambleford Wine Cellar (Not very necessary if logo is obviously shown)
- 42 Carrow Steet, Wexbury, Victoria, Australia 3275
- +61 3 9418 7360
- www.bramblefordwinecellar.example.au
- bramblefordwinecellar@mailbox.example
- Additional icons: Google, Instagram, Facebook, Twitter
4. Once again, forget it is a commercial card, make it special.

```html
<!DOCTYPE html>
<html lang="en">
<head>
<meta charset="utf-8">
<title>Brambleford Wine Cellar – Business Card</title>
<link href="https://fonts.googleapis.com/css2?family=Lato:wght@400;700;900&display=swap" rel="stylesheet">
<style>
  :root {
    --stage: #2b2b2d;
    --wine: #9c1e36;
    --crimson: #b3143b;
    --ink: #232325;
    --paper: #ffffff;
  }
  * { box-sizing: border-box; margin: 0; padding: 0; }
  html, body { width: 1200px; height: 878px; overflow: hidden; }
  body {
    background: var(--stage);
    font-family: "Lato", Arial, sans-serif;
    position: relative;
  }
  .card {
    position: absolute;
    left: 280px;
    width: 640px;
    height: 366px;
    box-shadow: 0 10px 28px rgba(0,0,0,.45);
  }
  .card--front { top: 46px; background: var(--wine); }
  .card--back { top: 466px; background: var(--paper); }

  .brand { display: flex; align-items: center; gap: 14px; }
  .brand__dot { width: 22px; height: 22px; border-radius: 50%; }
  .brand__name { font-weight: 700; letter-spacing: .12em; text-transform: uppercase; line-height: 1.2; white-space: nowrap; }

  .card--front .brand {
    position: absolute; left: 0; right: 0; top: 0; bottom: 0;
    justify-content: center;
  }
  .card--front .brand__dot { background: var(--paper); width: 30px; height: 30px; }
  .card--front .brand__name { color: var(--paper); font-size: 30px; }

  .card--back .brand { position: absolute; left: 40px; top: 52px; }
  .card--back .brand__dot { background: var(--wine); }
  .card--back .brand__name { color: var(--wine); font-size: 24px; }

  .contact {
    position: absolute; left: 40px; top: 168px;
    color: var(--ink); font-size: 14.5px; line-height: 1.4;
  }
  .contact__address { margin-bottom: 12px; }
  .contact__list { list-style: none; }
  .contact__list li { display: flex; align-items: center; gap: 12px; margin-bottom: 4px; white-space: nowrap; }
  .contact__list svg { width: 15px; height: 15px; flex: none; }
  .contact__accent { color: var(--crimson); }

  .person { position: absolute; right: 40px; top: 262px; text-align: right; white-space: nowrap; }
  .person__name { color: var(--crimson); font-weight: 900; font-size: 28px; letter-spacing: .01em; }
  .person__role { color: var(--ink); font-size: 17px; margin-top: 2px; }
</style>
</head>
<body>
  <section class="card card--front" aria-label="Card front">
    <div class="brand">
      <span class="brand__dot"></span>
      <span class="brand__name">Brambleford Wine Cellar</span>
    </div>
  </section>

  <section class="card card--back" aria-label="Card back">
    <div class="brand">
      <span class="brand__dot"></span>
      <span class="brand__name">Brambleford Wine Cellar</span>
    </div>

    <div class="contact">
      <p class="contact__address">42 Carrow Steet, Wexbury,<br>Victoria, Australia 3275</p>
      <ul class="contact__list">
        <li>
          <svg viewBox="0 0 16 16" aria-hidden="true"><path fill="var(--crimson)" d="M3.6 1.5l2.2 2.6-1.2 1.6c.9 2 2.5 3.6 4.6 4.6l1.6-1.2 2.6 2.2-1.3 2.2C7 13.2 2.8 9 2 3z"/></svg>
          <span>+61 3 9418 7360</span>
        </li>
        <li>
          <svg viewBox="0 0 16 16" aria-hidden="true"><rect x="1" y="3.5" width="14" height="9" fill="var(--crimson)"/><path d="M1.5 4l6.5 5 6.5-5" fill="none" stroke="#fff" stroke-width="1.2"/></svg>
          <span>bramblefordwinecellar@mailbox.example</span>
        </li>
        <li>
          <svg viewBox="0 0 16 16" aria-hidden="true"><g fill="none" stroke="var(--crimson)" stroke-width="1.3"><circle cx="8" cy="8" r="6.5"/><ellipse cx="8" cy="8" rx="2.8" ry="6.5"/><path d="M1.5 8h13M2.5 4.8h11M2.5 11.2h11"/></g></svg>
          <span>www.<span class="contact__accent">bramblefordwinecellar</span>.example.au</span>
        </li>
      </ul>
    </div>

    <div class="person">
      <p class="person__name">ELLIOT MARLOW</p>
      <p class="person__role">Founder &amp; CEO</p>
    </div>
  </section>
</body>
</html>
```